The Pixel Tap Business card.

A Simple card with our Logo and contact information. To give to investors and other professionals.

We are a nerd themed bar.
our target market is young professionals age 21+ but the real purpose of this business card is to present to potential investors and other professionals with our contact information. as we are still looking for funding before we start up.

I am partial to green and my partner likes red we are open to iteration.

Target Market(s)

Investors

Industry/Entity Type

Business

Contact Information for Business Card

Martin Hale (225) 730-6192 kent.h4711@mailnest.test Glen Porter (225) 968-5037 glenp318@mailnest.test

Font styles to use
Serif

Requirements
Nice to have
• Keep it simple but not boring.
• Use the Logos but feel free to edit them to match theme/colors.
• Keep the back clean and use one of the Logos.

```html
<!DOCTYPE html>
<html lang="en">
<head>
<meta charset="utf-8">
<title>The Pixel Tap – Business Card</title>
<link rel="stylesheet" href="https://fonts.googleapis.com/css2?family=Open+Sans:wght@400;600;700;800&display=swap">
<style>
  :root {
    --backdrop: #e6e6e6;
    --card: #ffffff;
    --ink: #111111;
    --accent: #e0202a;
    --rule: #8a8a8a;
    --shadow: rgba(0, 0, 0, 0.18);
  }
  * { box-sizing: border-box; margin: 0; padding: 0; }
  html, body {
    width: 1200px;
    height: 900px;
    overflow: hidden;
    background: var(--backdrop);
    font-family: "Open Sans", Arial, sans-serif;
    color: var(--ink);
  }
  .canvas { position: relative; width: 1200px; height: 900px; }

  .card {
    position: absolute;
    width: 560px;
    height: 320px;
    background: var(--card);
    box-shadow: 0 6px 18px var(--shadow);
  }
  .card--back { left: 560px; top: 90px; }
  .card--front { left: 90px; top: 470px; }

  .wordmark {
    position: absolute;
    left: 50%;
    transform: translateX(-50%);
    display: flex;
    align-items: center;
    gap: 14px;
    white-space: nowrap;
    font-weight: 800;
    letter-spacing: 1px;
    text-transform: uppercase;
    color: var(--ink);
  }
  .wordmark__dot {
    width: 30px;
    height: 30px;
    border-radius: 50%;
    background: var(--accent);
    flex: none;
  }
  .card--back .wordmark { top: 128px; font-size: 46px; }
  .card--front .wordmark { top: 48px; font-size: 40px; }

  .divider {
    position: absolute;
    left: 40px;
    right: 40px;
    top: 150px;
    border-top: 1px solid var(--rule);
  }

  .contacts {
    position: absolute;
    left: 0;
    right: 0;
    top: 176px;
    display: flex;
    justify-content: center;
    gap: 28px;
    font-size: 15px;
    line-height: 1.55;
  }
  .contact { display: flex; flex-direction: column; }
  .contact--left { align-items: flex-end; text-align: right; }
  .contact--right { align-items: flex-start; text-align: left; }
  .contact__name {
    color: var(--accent);
    font-weight: 700;
    font-size: 17px;
    margin-bottom: 2px;
  }
  .contact__line { display: flex; align-items: center; gap: 9px; }
  .icon { width: 12px; height: 12px; fill: var(--accent); flex: none; }
</style>
</head>
<body>
<main class="canvas">

  <section class="card card--back" aria-label="Card back">
    <div class="wordmark"><span class="wordmark__dot"></span>The Pixel Tap</div>
  </section>

  <section class="card card--front" aria-label="Card front">
    <div class="wordmark"><span class="wordmark__dot"></span>The Pixel Tap</div>
    <div class="divider"></div>

    <div class="contacts">
      <div class="contact contact--left">
        <div class="contact__name">Martin Hale</div>
        <div class="contact__line">(225) 730-6192
          <svg class="icon" viewBox="0 0 24 24" aria-hidden="true"><path d="M6.6 10.8a15.1 15.1 0 0 0 6.6 6.6l2.2-2.2c.3-.3.7-.4 1-.2 1.1.4 2.3.6 3.6.6.6 0 1 .4 1 1V20c0 .6-.4 1-1 1A17 17 0 0 1 3 4c0-.6.4-1 1-1h3.5c.6 0 1 .4 1 1 0 1.3.2 2.5.6 3.6.1.3 0 .7-.2 1z"/></svg>
        </div>
        <div class="contact__line">kent.h4711@mailnest.test
          <svg class="icon" viewBox="0 0 24 24" aria-hidden="true"><path d="M2 5h20v14H2z M3 6l9 7 9-7" /></svg>
        </div>
      </div>

      <div class="contact contact--right">
        <div class="contact__name">Glen Porter</div>
        <div class="contact__line">
          <svg class="icon" viewBox="0 0 24 24" aria-hidden="true"><path d="M6.6 10.8a15.1 15.1 0 0 0 6.6 6.6l2.2-2.2c.3-.3.7-.4 1-.2 1.1.4 2.3.6 3.6.6.6 0 1 .4 1 1V20c0 .6-.4 1-1 1A17 17 0 0 1 3 4c0-.6.4-1 1-1h3.5c.6 0 1 .4 1 1 0 1.3.2 2.5.6 3.6.1.3 0 .7-.2 1z"/></svg>
          (225) 968-5037
        </div>
        <div class="contact__line">
          <svg class="icon" viewBox="0 0 24 24" aria-hidden="true"><path d="M2 5h20v14H2z M3 6l9 7 9-7" /></svg>
          glenp318@mailnest.test
        </div>
      </div>
    </div>
  </section>

</main>
</body>
</html>
```